I need a CD cover (simple single CD -- NOT jewel case) for my new CD. This is a very small independent project -- probably 100 - 200 copies to be made in total. The name of the CD is "Folded Lanterns". My name (artist) is ned valko (I prefer lower case for my name). I just want an interesting design on the front cover that has both the CD name and my name (no photo) -- just something that looks cool -- I'm open to any and all ideas. The back should contain the enclosed photo -- I am open to the photo being any size -- even very small if that looks best. The front cover design will also need to be ON the CD itself (adapted as needed). I am not concerned with the design of the front having any relationship to the music -- I just want something that is attractive and looks cool.
Look and feel
Each slider illustrates characteristics of the customer's brand and the style your logo design should communicate.

```html
<!DOCTYPE html>
<html lang="en">
<head>
<meta charset="utf-8">
<title>ned valko — Folded Lanterns</title>
<link rel="stylesheet" href="https://fonts.googleapis.com/css2?family=Josefin+Sans:wght@100;200&display=swap">
<style>
  :root {
    --night: #0b0c35;
    --deep-blue: #1a2a6e;
    --trail-blue: #2f4fa0;
    --teal: #2f9a92;
    --moss: #6f8a3a;
    --olive: #8a8a35;
    --ember: #5a2325;
    --ink-white: #ffffff;
  }
  html, body {
    margin: 0;
    padding: 0;
    width: 1200px;
    height: 1200px;
    overflow: hidden;
    background: var(--night);
  }
  .cover {
    position: relative;
    width: 1200px;
    height: 1200px;
    overflow: hidden;
    font-family: "Josefin Sans", "Helvetica Neue", Arial, sans-serif;
    color: var(--ink-white);
  }
  .cover__artwork {
    position: absolute;
    inset: 0;
    background:
      radial-gradient(ellipse 260px 200px at 690px 780px, var(--olive) 0%, rgba(138,138,53,0) 100%),
      radial-gradient(ellipse 380px 260px at 360px 960px, var(--ember) 0%, rgba(90,35,37,0) 100%),
      radial-gradient(ellipse 420px 360px at 520px 640px, var(--moss) 0%, rgba(111,138,58,0) 100%),
      radial-gradient(ellipse 420px 340px at 600px 420px, var(--teal) 0%, rgba(47,154,146,0) 100%),
      radial-gradient(ellipse 700px 620px at 900px 420px, var(--trail-blue) 0%, rgba(47,79,160,0) 100%),
      linear-gradient(180deg, var(--deep-blue) 0%, var(--night) 30%, var(--deep-blue) 55%, var(--night) 100%);
  }
  .cover__shade {
    position: absolute;
    inset: 0;
    background:
      linear-gradient(180deg, rgba(11,12,53,0) 78%, var(--night) 100%),
      linear-gradient(90deg, rgba(11,12,53,0.85) 0%, rgba(11,12,53,0) 18%);
  }
  .cover__artist {
    position: absolute;
    left: 26px;
    top: 16px;
    margin: 0;
    font-weight: 200;
    font-size: 84px;
    line-height: 1;
    letter-spacing: -1px;
    text-transform: none;
    white-space: nowrap;
  }
  .cover__title {
    position: absolute;
    right: 40px;
    top: 996px;
    margin: 0;
    font-weight: 200;
    font-size: 92px;
    line-height: 86px;
    letter-spacing: -1px;
    text-align: right;
    text-transform: uppercase;
    white-space: nowrap;
  }
  .cover__title span { display: block; }
</style>
</head>
<body>
  <main class="cover">
    <div class="cover__artwork" role="img" aria-label="Night photograph of swirling blue star trails over a dark field, with a lone silhouetted figure standing in a glow of teal, green and rust"></div>
    <div class="cover__shade" aria-hidden="true"></div>
    <h2 class="cover__artist">ned valko</h2>
    <h1 class="cover__title"><span>Folded</span><span>Lanterns</span></h1>
  </main>
</body>
</html>
```